"9" length 6.5" height" post card of pennyvault.net trying to get people to text the word YES to our phone number to access our latest stock picks. or tickerleaf.io we own both of them. Call to action. Get winnin stock picks sign up now text the word "YES" to 888-412-7390. must haves: " track record 2023: 477.8%" "#1 stock picking newsletter in the U.S.A." " Disclaimer: The materials and content provided by PennyVault.net, including but not limited to our website, emails, blogs, and text messages (collectively, the "Materials"), are intended for general information purposes only and do not constitute financial, legal, or investment advice. PennyVault.net is engaged in the business of marketing and advertising companies for compensation. The information contained in the Materials is not, and should not be read as, an offer or recommendation to buy or sell any securities. All content is provided for informational and educational purposes only. PennyVault.net and its staff are not licensed investment advisors, brokers, or dealers. Any content provided by us is not intended to solicit or recommend any investment and should not be used as the basis for any investment decisions. We do not provide investment advice, endorse any financial product, or suggest that any particular investment or strategy is suitable for any specific person. PennyVault.net receives compensation from the companies featured in our alerts, emails, and other Materials for marketing and advertising services. The existence of such compensation may influence the content, topics, or posts made in the Materials. Investing in stocks, especially penny stocks, involves a high level of risk and may not be suitable for all investors. The possibility exists that you could sustain a loss of some or all of your initial investment. Therefore, you should not invest money that you cannot afford to lose. The performance figures stated in the Materials, including but not limited to a track record of 477% in 2023, are hypothetical and should not be considered indicative of future results. Past performance is not necessarily indicative of future results. Individual results may vary, and the examples used in the Materials are not guaranteed to occur. You are encouraged to perform your own due diligence and consult with a qualified financial advisor before making any investment decisions. PennyVault.net and its Materials should not be used as the sole basis for any investment decision. We make no representation or warranty as to the accuracy, completeness, or reliability of the information contained in the Materials. The content provided by PennyVault.net and in its newsletter is intended for entertainment purposes only. Acknowledgment: By using PennyVault.net's services, joining our site, or subscribing to our email/blog list, you acknowledge that you have read, understood, and agree to be bound by the terms of this disclaimer. If you do not agree with these terms, you should not use our services or subscribe to our Materials

."

Target Market(s)

investors

Industry/Entity Type

financial

Colors
0054AA
0677BA
7BADD7
CADEEF
E8F1F8
00AB8E
00BBA5
67D7C9
C6EFE9
E9F9F6
59FF00
82FF00
B8FF75
E3FFCB
F4FFEA

Requirements
Must have
• " track record 2023: 477.8%" "#1 stock picking newsletter in the U.S.A." "Disclaimer: The materials and content provided by PennyVault.net, including but not limited to our website, emails, blogs, and text messages (collectively, the "Materials"), are intended for general information purposes only and do not constitute financial, legal, or investment advice. PennyVault.net is engaged in the business of marketing and advertising companies for compensation. The information contained in the Materials is not, and should not be read as, an offer or recommendation to buy or sell any securities. All content is provided for informational and educational purposes only. PennyVault.net and its staff are not licensed investment advisors, brokers, or dealers. Any content provided by us is not intended to solicit or recommend any investment and should not be used as the basis for any investment decisions. We do not provide investment advice, endorse any financial product, or suggest that any particular investment or strategy is suitable for any specific person. PennyVault.net receives compensation from the companies featured in our alerts, emails, and other Materials for marketing and advertising services. The existence of such compensation may influence the content, topics, or posts made in the Materials. Investing in stocks, especially penny stocks, involves a high level of risk and may not be suitable for all investors. The possibility exists that you could sustain a loss of some or all of your initial investment. Therefore, you should not invest money that you cannot afford to lose. The performance figures stated in the Materials, including but not limited to a track record of 477% in 2023, are hypothetical and should not be considered indicative of future results. Past performance is not necessarily indicative of future results. Individual results may vary, and the examples used in the Materials are not guaranteed to occur. You are encouraged to perform your own due diligence and consult with a qualified financial advisor before making any investment decisions. PennyVault.net and its Materials should not be used as the sole basis for any investment decision. We make no representation or warranty as to the accuracy, completeness, or reliability of the information contained in the Materials. The content provided by PennyVault.net and in its newsletter is intended for entertainment purposes only. Acknowledgment: By using PennyVault.net's services, joining our site, or subscribing to our email/blog list, you acknowledge that you have read, understood, and agree to be bound by the terms of this disclaimer. If you do not agree with these terms, you should not use our services or subscribe to our Materials."
Nice to have
• call to action: Get exclusive stock picks delivered directly to your phone. Text "YES" to [888-412-7390] to receive your first stock pick

```html
<!DOCTYPE html>
<html lang="en">
<head>
<meta charset="utf-8">
<title>PennyVault.net — Text YES for Stock Picks</title>
<link rel="stylesheet" href="https://fonts.googleapis.com/css2?family=Jost:wght@300;400;500;600&display=swap">
<style>
  :root {
    --page-bg: #ececec;
    --navy-deep: #0d1828;
    --navy: #12203a;
    --navy-low: #0f1b2c;
    --glow-blue: #1b8fd6;
    --glow-cyan: #5fc8f2;
    --white: #ffffff;
    --ink: #1e2227;
  }
  * { margin: 0; padding: 0; box-sizing: border-box; }
  html, body {
    width: 1200px; height: 1200px; overflow: hidden;
    background: var(--page-bg);
  }
  body { position: relative; font-family: "Jost", sans-serif; }

  .postcard {
    position: absolute; left: 189px; top: 30px;
    width: 822px; height: 1140px;
    background: linear-gradient(180deg, var(--navy-deep) 0%, var(--navy) 55%, var(--navy-low) 100%);
    overflow: hidden;
    color: var(--white);
  }

  .chart-art {
    position: absolute; left: 53px; top: 119px; width: 345px; height: 424px;
    background:
      radial-gradient(ellipse at 45% 55%, rgba(95,200,242,0.55) 0%, rgba(27,143,214,0.35) 35%, rgba(18,32,58,0) 72%),
      linear-gradient(180deg, rgba(27,143,214,0.15), rgba(27,143,214,0.35));
    border-radius: 4px;
  }

  .shapes { position: absolute; inset: 0; width: 822px; height: 1140px; }

  .headline {
    position: absolute; right: 100px; top: 103px;
    text-align: right; text-transform: uppercase;
    font-weight: 500; font-size: 29px; line-height: 40px; letter-spacing: 0.3px;
  }

  .bubble-text {
    position: absolute; left: 367px; top: 388px;
    font-weight: 300; font-size: 26px; line-height: 33px;
  }
  .bubble-text .keyword { font-weight: 600; font-size: 34px; }

  .track-label {
    position: absolute; left: 114px; top: 728px;
    color: var(--ink); line-height: 1;
  }
  .track-label .small { display: block; font-size: 16px; font-weight: 400; }
  .track-label .year { display: block; font-size: 40px; font-weight: 400; margin-top: 0; }

  .stat {
    position: absolute; left: 431px; top: 700px;
  }
  .stat .figure { font-size: 54px; font-weight: 600; line-height: 56px; }
  .stat .claim { font-size: 26px; font-weight: 300; line-height: 32px; }

  .disclaimer {
    position: absolute; left: 46px; top: 868px; width: 730px;
    font-size: 10.2px; line-height: 12.4px; font-weight: 400;
    text-align: justify; color: var(--white);
  }
  .disclaimer strong { font-weight: 600; }
</style>
</head>
<body>
  <main class="postcard">
    <div class="chart-art" role="img" aria-label="Glowing blue rising stock chart with bars and an upward arrow above a tablet"></div>

    <svg class="shapes" viewBox="0 0 822 1140" aria-hidden="true">
      <path class="lower-band" d="M0,850 C120,810 220,795 822,790 L822,1140 L0,1140 Z" fill="#0c1624"/>
      <ellipse cx="500" cy="650" rx="210" ry="16" fill="#000" opacity="0.35"/>
      <!-- speech bubble -->
      <path d="M605,378 Q645,330 632,256 Q668,330 690,404 Z" fill="#0f1c31" stroke="#fff" stroke-width="5" stroke-linejoin="round"/>
      <ellipse cx="497" cy="490" rx="225" ry="146" fill="#0f1c31" stroke="#fff" stroke-width="6"/>
      <path d="M605,378 Q645,330 632,256 Q668,330 690,404 Z" fill="#0f1c31"/>
      <!-- arrow -->
      <path d="M0,726 L278,726 L278,696 L345,759 L278,822 L278,795 L0,795 Z" fill="#fff"/>
    </svg>

    <h1 class="headline">Get exclusive stock<br>picks delivered directly<br>to your phone</h1>

    <p class="bubble-text">Text <span class="keyword">"YES"</span><br>to [888-412-7390]<br>to receive<br>your first stock pick</p>

    <p class="track-label"><span class="small">Track record</span><span class="year">2023:</span></p>

    <div class="stat">
      <p class="figure">477.8%</p>
      <p class="claim">#1 stock picking<br>newsletter in the U.S.A.</p>
    </div>

    <p class="disclaimer"><strong>Disclaimer:</strong> This report/release is a commercial advertisement and is for general information purposes ONLY. We are engaged in the business of marketing and advertising companies for compensation. Never invest in any stock featured on our site or emails unless you can afford to lose your entire investment. This disclaimer is to be read and fully understood before using our services, joining our site or our email/blog list. The track record, gains, upside, and/or losses mentioned are all hypothetical and should not be considered as the basis for investment. Penny-stock trading involves substantial risk, so always research every alert before trading, consult with a licensed professional before trading, only invest what you can afford to lose, and always trade with caution. Readers should independently investigate and fully understand all risks before investing. Results listed above are NOT typical and individual results may and most likely will vary. PennyVault and its staff are NOT licensed investment advisors or broker/dealers of any kind. Alerts are not a solicitation or recommendation to buy/sell/hold securities but merely investment ideas that should NEVER serve as the basis of your trading decisions. PennyVault and its newsletter are for entertainment purposes only. This website and its reports are for general information purposes as we are engaged in the business of marketing and advertising companies for monetary compensation. Any investment decision should be discussed with a financial adviser before taking place."</p>
  </main>
</body>
</html>
```